BARRIER BANNER KTV

I am looking for a visual for a banner
3 meters long by 1 high.
In the same theme as the visual identity of the company.
As simple as possible without overloading

There must be the LOGO, the title VOLTARIS SERVICES TECHNIQUES

_________________________

I am looking for a visual for a banner (barrier banner)
3 meters long by 1 high.

AIR CONDITIONING HEATING VENTILATION
04 52 31 69 14

Font styles to use
Sans Serif

Colors
33b8a4
00a990
33a6d7
0493ce
3176b5
0355a3
ffffff

Requirements
Should not have
• No photo
No photo

```html
<!DOCTYPE html>
<html lang="fr">
<head>
<meta charset="utf-8">
<title>KTV – Barrier Banner</title>
<link rel="stylesheet" href="https://fonts.googleapis.com/css2?family=Montserrat:wght@600;800&display=swap">
<style>
  :root {
    --stage: #8a8a8a;
    --sky: #a3d7e8;
    --floor: #004a6e;
    --ink: #2b3640;
    --white: #ffffff;
    --teal: #33b8a4;
    --green: #00a990;
    --blue: #0355a3;
    --illustration-top: #c9e6ef;
    --illustration-bottom: #5f86b6;
  }
  * { margin: 0; padding: 0; box-sizing: border-box; }
  html, body {
    width: 1200px; height: 516px; overflow: hidden;
    background: var(--stage);
    font-family: "Montserrat", Arial, sans-serif;
  }
  .banner {
    position: absolute; left: 20px; top: 64px;
    width: 1160px; height: 387px;
    background: var(--sky);
    overflow: hidden;
  }
  .floor-band {
    position: absolute; left: 0; right: 0; top: 323px; bottom: 0;
    background: var(--floor);
  }
  .illustration {
    position: absolute; left: 36px; top: 59px; width: 421px; height: 290px;
    background: linear-gradient(180deg, var(--illustration-top), var(--illustration-bottom));
    border-radius: 4px;
  }
  .logo-tab {
    position: absolute; left: 979px; top: 0; width: 141px; height: 93px;
    background: var(--white);
    border-radius: 0 0 10px 10px;
    display: flex; align-items: center; justify-content: center;
  }
  .logo-name {
    font-weight: 800; font-size: 46px; color: var(--ink); letter-spacing: 1px;
  }
  .title {
    position: absolute; left: 534px; top: 48px;
    font-weight: 800; font-size: 44px; line-height: 43px;
    color: var(--ink); letter-spacing: 0.5px;
  }
  .services { position: absolute; left: 0; top: 0; width: 100%; height: 100%; pointer-events: none; }
  .service {
    position: absolute; top: 198px; width: 200px; margin-left: -100px;
    display: flex; flex-direction: column; align-items: center;
  }
  .service-icon { width: 58px; height: 66px; }
  .service-label {
    margin-top: 10px; font-weight: 600; font-size: 19px; color: var(--ink);
    white-space: nowrap; letter-spacing: 0.3px;
  }
  .call {
    position: absolute; left: 534px; top: 330px;
    font-weight: 600; font-size: 40px; line-height: 50px;
    color: var(--white); letter-spacing: 1px; white-space: nowrap;
  }
</style>
</head>
<body>
<svg width="0" height="0" style="position:absolute">
  <defs>
    <linearGradient id="hex-fill" x1="0" y1="0" x2="1" y2="1">
      <stop offset="0" stop-color="#00a990"/>
      <stop offset="0.55" stop-color="#0b7a8a"/>
      <stop offset="1" stop-color="#0355a3"/>
    </linearGradient>
  </defs>
</svg>

<main class="banner">
  <div class="floor-band"></div>
  <div class="illustration" role="img" aria-label="Illustration de deux techniciens installant un climatiseur mural et une unité extérieure, près d'une fenêtre, d'une plante et d'une caisse à outils"></div>

  <div class="logo-tab"><span class="logo-name">KTV</span></div>

  <h1 class="title">VOLTARIS<br>SERVICES<br>TECHNIQUES</h1>

  <section class="services">
    <div class="service" style="left:629px">
      <svg class="service-icon" viewBox="0 0 58 66">
        <polygon points="29,2 55,17 55,49 29,64 3,49 3,17" fill="url(#hex-fill)" stroke="#fff" stroke-width="2"/>
        <g fill="none" stroke="#fff" stroke-width="2" stroke-linecap="round">
          <rect x="15" y="24" width="28" height="12" rx="2"/>
          <line x1="19" y1="32" x2="39" y2="32"/>
          <path d="M29 13v7M25.5 14.5l7 4M32.5 14.5l-7 4"/>
          <path d="M23 40c2 2-2 4 0 6M29 40c2 2-2 4 0 6M35 40c2 2-2 4 0 6"/>
        </g>
      </svg>
      <span class="service-label">AIR CONDITIONING</span>
    </div>
    <div class="service" style="left:792px">
      <svg class="service-icon" viewBox="0 0 58 66">
        <polygon points="29,2 55,17 55,49 29,64 3,49 3,17" fill="url(#hex-fill)" stroke="#fff" stroke-width="2"/>
        <path d="M29 14c2 7 10 11 10 20a10 10 0 0 1-20 0c0-5 3-8 5-10 0 4 2 6 4 6-2-6 1-12 1-16z" fill="#fff"/>
      </svg>
      <span class="service-label">HEATING</span>
    </div>
    <div class="service" style="left:929px">
      <svg class="service-icon" viewBox="0 0 58 66">
        <polygon points="29,2 55,17 55,49 29,64 3,49 3,17" fill="url(#hex-fill)" stroke="#fff" stroke-width="2"/>
        <g fill="none" stroke="#fff" stroke-width="2" stroke-linejoin="round">
          <circle cx="29" cy="33" r="3"/>
          <path d="M29 30c-3-6 0-12 6-12 3 4 0 9-6 12z"/>
          <path d="M31.6 34.5c6.5 0 10 5 7 10-5 1-8-3-7-10z"/>
          <path d="M26.4 34.5c-3.5 5.5-9.5 6-12 1 1.5-5 6.5-5 12-1z"/>
        </g>
      </svg>
      <span class="service-label">VENTILATION</span>
    </div>
  </section>

  <p class="call">CALL 04 52 31 69 14</p>
</main>
</body>
</html>
```